HVAC Parts Distributor Website

We are working with an HVAC parts distributor to design a website. They primarily work with HVAC contractors.
They are similar to: https://www.quellbrookparts.com, and https://www.ventoriadepot.com
Thank you for taking the time to consider designing a website for us. We are web developers based in Stockton, CA, USA. Most of our projects go through the same process. Understanding this process may help you win a project with us. We custom-code all of our websites in-house. We don’t have any requirements as to what tools you use for your design, but we ask that you follow these guidelines.
IMAGES:
If you use any images or icons in the design, we ask that you have a link to the asset so we can purchase the image/icon. Most of the designs we submit do not have the customer’s images on them unless they have some great images. Be creative; show us the feeling you are trying to portray with your image choices. Use any royalty-free site you choose. We subscribe to Zephrin and mainly use their images, but we can purchase images outside of Zephrin.
FONTS:
We ask that you identify the fonts you’re using in the design. This can be done in a message if you want. We typically use Quorvel Fonts and Zephrin Fonts.
CONTENT:
We're always open to different content and ideas. We often submit designs with stock images so the client can see our vision. We typically take pictures after the website launch to use their images with our vision. Lorem Ipsum is fine for paragraphs, but we ask that you make the Headers with correct English. We want to be able to show the vision and identify the sections of the website.
INSPIRATION:
We typically add a couple of links in the brief of websites we like to help you get started in your design.
REVISIONS:
We do not often ask for revisions of the designs unless we see something in the design that may not appeal to the client. If there are slight changes that we want to make, we simply do that in the development process.
FEEDBACK:
We rarely give feedback on designs during the design process. We are working on many website projects and do not have the time to give feedback. We usually respond if your request is well thought out and asks specific questions, but a note asking “feedback, please” usually goes unanswered.

```html
<!DOCTYPE html>
<html lang="en">
<head>
<meta charset="utf-8">
<title>Kestral HVAC Supply</title>
<link href="https://fonts.googleapis.com/css2?family=Roboto:wght@400;500;700;900&display=swap" rel="stylesheet">
<style>
:root{
  --green:#93ab0e;
  --green-dark:#7f950a;
  --dark:#2b2728;
  --ink:#222;
  --muted:#6b6b6b;
  --white:#fff;
}
*{margin:0;padding:0;box-sizing:border-box}
html,body{width:1200px;height:3645px;overflow:hidden}
body{font-family:'Roboto',sans-serif;color:var(--ink);background:var(--white);position:relative}
a{color:inherit;text-decoration:none}
.abs{position:absolute}

/* buttons */
.btn{position:absolute;display:flex;align-items:center;justify-content:center;font-weight:700;font-size:17px;color:var(--white);height:50px}
.btn .face{position:absolute;inset:0 14px 0 0;background:var(--green);clip-path:polygon(10px 0,100% 0,calc(100% - 10px) 100%,0 100%)}
.btn .stripe{position:absolute;top:0;right:0;width:13px;height:100%;background:var(--green);clip-path:polygon(8px 0,13px 0,5px 100%,0 100%)}
.btn span{position:relative;margin-right:14px}
.btn.dark .face,.btn.dark .stripe{background:var(--dark)}

/* header */
.site-header{position:absolute;top:0;left:0;width:1200px;height:95px;border-top:4px solid var(--dark);background:var(--white)}
.brand{position:absolute;left:111px;top:30px;display:flex;align-items:center;gap:10px;font-weight:900;font-size:24px;color:var(--dark);letter-spacing:.5px}
.brand .mark{width:22px;height:22px;background:var(--green)}
.main-nav{position:absolute;top:46px;left:0;font-size:12.5px;font-weight:500;color:#333}
.main-nav a{position:absolute;white-space:nowrap}

/* hero */
.hero{position:absolute;top:95px;left:0;width:1200px;height:612px;background:var(--dark);overflow:hidden}
.hero-photo{position:absolute;inset:0}
.hero-kicker{position:absolute;left:111px;top:142px;color:var(--white);font-weight:900;font-size:37px}
.hero-title{position:absolute;left:111px;top:188px;color:var(--white);font-weight:900;font-size:62px;line-height:70px}

/* how it works */
.how{position:absolute;top:707px;left:0;width:1200px;height:1093px}
.section-title{position:absolute;left:0;width:1200px;text-align:center;font-weight:900;font-size:48px;color:var(--ink)}
.section-lead{position:absolute;left:0;width:1200px;text-align:center;font-size:14px;line-height:26px;color:var(--muted)}
.how svg{position:absolute;top:0;left:0}
.step{position:absolute;width:200px;text-align:center}
.step h3{font-size:18px;font-weight:700;color:var(--ink);margin-bottom:10px}
.step p{font-size:11.5px;line-height:20px;color:var(--muted);padding:0 10px}

/* about */
.about{position:absolute;top:1800px;left:0;width:1200px;height:610px;background:var(--green);overflow:hidden}
.about h2{position:absolute;left:111px;top:82px;font-size:48px;font-weight:900;color:var(--white)}
.about .copy{position:absolute;left:111px;top:155px;width:445px;color:var(--white);font-size:13.5px;line-height:25.7px}
.about .copy p+p{margin-top:26px}

/* customers */
.customers{position:absolute;top:2410px;left:0;width:1200px;height:820px}
.review{position:absolute;top:246px;width:474px;height:382px;background:var(--white);box-shadow:0 2px 14px rgba(0,0,0,.12);text-align:center}
.review svg{margin-top:46px}
.review .quote{margin:12px auto 0;width:376px;font-size:12.5px;line-height:25px;color:var(--muted)}
.review .name{margin-top:20px;font-weight:700;font-size:16px;color:var(--ink)}
.review .place{margin-top:6px;font-size:12px;color:var(--muted)}

/* footer */
.site-footer{position:absolute;top:3229px;left:0;width:1200px;height:416px;background:var(--dark);color:var(--white)}
.newsletter-title{position:absolute;left:111px;top:76px;font-weight:900;font-size:27px}
.newsletter-form{position:absolute;left:600px;top:61px;width:488px;height:66px;background:var(--green);border:3px solid var(--green)}
.newsletter-form label{position:absolute;left:25px;top:22px;font-size:13px;color:var(--white)}
.newsletter-form .send{position:absolute;right:3px;top:3px;width:58px;height:54px;background:var(--dark);display:flex;align-items:center;justify-content:center}
.footer-brand{position:absolute;left:0;width:1200px;top:175px;text-align:center;font-weight:900;font-size:32px;letter-spacing:.5px}
.footer-nav{position:absolute;left:0;width:1200px;top:266px;text-align:center;font-size:15px}
.footer-nav a{margin:0 28px}
.footer-nav i{font-style:normal}
.copyright{position:absolute;left:0;width:1200px;top:315px;text-align:center;font-size:12px}
.socials{position:absolute;top:354px;left:529px;display:flex;gap:13px}
.socials span{width:26px;height:26px;border-radius:50%;background:var(--green)}
</style>
</head>
<body>

<header class="site-header">
  <div class="brand"><span class="mark"></span>Kestral HVAC Supply</div>
  <nav class="main-nav">
    <a style="left:445px">HOME</a>
    <a style="left:522px">ABOUT US</a>
    <a style="left:625px">SERVICES</a>
    <a style="left:725px">HOW IT WORKS</a>
    <a style="left:857px">REVIEWS</a>
  </nav>
  <a class="btn" style="left:940px;top:23px;width:148px;height:50px"><i class="face"></i><i class="stripe"></i><span>Contact Us</span></a>
</header>

<section class="hero">
  <svg class="hero-photo" width="1200" height="612" role="img" aria-label="Photo of a family relaxing together on a sofa at home">
    <defs><linearGradient id="heroGrad" x1="0" y1="0" x2="1" y2="1"><stop offset="0" stop-color="#e8e6e2"/><stop offset=".6" stop-color="#c9c3bc"/><stop offset="1" stop-color="#8d8179"/></linearGradient></defs>
    <polygon points="850,0 1200,0 1200,612 360,612" fill="url(#heroGrad)"/>
  </svg>
  <div class="hero-kicker">WELCOME TO</div>
  <h1 class="hero-title">KESTRAL HVAC<br>SUPPLY</h1>
  <a class="btn" style="left:111px;top:366px;width:200px"><i class="face"></i><i class="stripe"></i><span>Get Started</span></a>
</section>

<section class="how">
  <h2 class="section-title" style="top:78px">HOW IT WORKS</h2>
  <p class="section-lead" style="top:148px">Lorem Ipsum is simply dummy text of the printing and typesetting industry. Lorem Ipsum has been the industry's standard dummy text ever since<br>the 1500s, when an unknown printer took a galley of type and scrambled it to make a type specimen book. It has survived not only five<br>centuries, but also the leap into electronic typesetting</p>

  <svg width="1200" height="1093" aria-hidden="true">
    <defs><filter id="soft" x="-20%" y="-20%" width="140%" height="140%"><feDropShadow dx="0" dy="3" stdDeviation="6" flood-color="#000" flood-opacity=".12"/></filter></defs>
    <g fill="#fff" filter="url(#soft)">
      <polygon points="415,354 538,416 538,542 415,604 292,542 292,416"/>
      <polygon points="783,354 906,416 906,542 783,604 660,542 660,416"/>
      <polygon points="233,654 356,716 356,842 233,904 110,842 110,716"/>
      <polygon points="599,654 722,716 722,842 599,904 476,842 476,716"/>
      <polygon points="965,654 1088,716 1088,842 965,904 842,842 842,716"/>
    </g>
    <polyline points="232,542 416,715 599,544 783,716 965,544" fill="none" stroke="#333" stroke-width="1"/>
    <g>
      <polygon points="232,502 266,522 266,562 232,582 198,562 198,522" fill="var(--green)"/>
      <polygon points="416,675 450,695 450,735 416,755 382,735 382,695" fill="var(--dark)"/>
      <polygon points="599,504 633,524 633,564 599,584 565,564 565,524" fill="var(--green)"/>
      <polygon points="783,676 817,696 817,736 783,756 749,736 749,696" fill="var(--dark)"/>
      <polygon points="965,504 999,524 999,564 965,584 931,564 931,524" fill="var(--green)"/>
    </g>
    <g fill="#fff" font-family="Roboto,sans-serif" font-weight="700" font-size="21" text-anchor="middle">
      <text x="232" y="549">01</text><text x="416" y="722">02</text><text x="599" y="551">03</text><text x="783" y="723">04</text><text x="965" y="551">05</text>
    </g>
    <g>
      <circle cx="415" cy="328" r="51" fill="var(--green)"/><circle cx="415" cy="328" r="42" fill="#fff"/><circle cx="415" cy="328" r="35" fill="var(--green)"/>
      <circle cx="784" cy="328" r="51" fill="var(--dark)"/><circle cx="784" cy="328" r="42" fill="#fff"/><circle cx="784" cy="328" r="35" fill="var(--dark)"/>
      <circle cx="233" cy="933" r="51" fill="var(--dark)"/><circle cx="233" cy="933" r="42" fill="#fff"/><circle cx="233" cy="933" r="35" fill="var(--dark)"/>
      <circle cx="599" cy="933" r="51" fill="var(--green)"/><circle cx="599" cy="933" r="42" fill="#fff"/><circle cx="599" cy="933" r="35" fill="var(--green)"/>
      <circle cx="965" cy="933" r="51" fill="var(--dark)"/><circle cx="965" cy="933" r="42" fill="#fff"/><circle cx="965" cy="933" r="35" fill="var(--dark)"/>
    </g>
    <g fill="#fff"><rect x="396" y="316" width="24" height="18" rx="2"/><path d="M421 321h8l6 7v6h-14z"/><circle cx="403" cy="337" r="4"/><circle cx="427" cy="337" r="4"/></g>
    <g fill="#fff"><rect x="770" y="322" width="28" height="7"/><rect x="772" y="330" width="24" height="16"/><rect x="782" y="322" width="4" height="24" fill="var(--dark)"/><path d="M784 321c-6-9-14-3-8 0zM784 321c6-9 14-3 8 0z"/></g>
    <g><path d="M219 935l14-16h14v14l-16 16z" fill="#fff"/><circle cx="241" cy="925" r="2.5" fill="var(--dark)"/><text x="236" y="943" fill="var(--dark)" font-family="Roboto,sans-serif" font-weight="700" font-size="11" text-anchor="middle">$</text></g>
    <g fill="none" stroke="#fff" stroke-width="3"><path d="M582 933a17 17 0 0 1 29-12"/><path d="M616 933a17 17 0 0 1-29 12"/></g>
    <path d="M608 915l6 9-10 0z M590 951l-6-9 10 0z" fill="#fff"/>
    <circle cx="599" cy="933" r="10" fill="#fff"/>
    <text x="599" y="938" fill="var(--green)" font-family="Roboto,sans-serif" font-weight="700" font-size="13" text-anchor="middle">$</text>
    <path d="M955 917c3-2 6 4 7 7s-3 4-2 6 5 7 8 8 3-3 6-2 8 5 6 8-6 5-10 4-18-11-19-19 1-10 4-12z" fill="#fff"/>
  </svg>

  <div class="step" style="left:315px;top:420px"><h3>Free Shipping</h3><p>Lorem Ipsum is simply dummy text of the printing and typesetting industry.</p></div>
  <div class="step" style="left:683px;top:420px"><h3>Exclusive Gear</h3><p>Lorem Ipsum is simply dummy text of the printing and typesetting industry.</p></div>
  <div class="step" style="left:133px;top:740px"><h3>Lower Prices</h3><p>Lorem Ipsum is simply dummy text of the printing and typesetting industry.</p></div>
  <div class="step" style="left:499px;top:740px"><h3>Free Returns</h3><p>Lorem Ipsum is simply dummy text of the printing and typesetting industry.</p></div>
  <div class="step" style="left:865px;top:740px"><h3>Dedicated Phone Line</h3><p>Lorem Ipsum is simply dummy text of the printing and typesetting industry.</p></div>
</section>

<section class="about">
  <svg class="abs" style="top:0;left:0" width="1200" height="610" role="img" aria-label="Dark decorative panel">
    <polygon points="640,0 1200,0 1200,610 470,610" fill="var(--dark)"/>
  </svg>
  <h2>ABOUT US</h2>
  <div class="copy">
    <p>Lorem Ipsum is simply dummy text of the printing and typesetting industry. Lorem Ipsum has been the industry's standard dummy text ever since the 1500s, when an unknown printer took a galley of type and scrambled it to make a type specimen book. It has survived not only five centuries, but also the leap into electronic typesetting, remaining essentially unchanged.</p>
    <p>It was popularised in the 1960s with the release of Veltrane sheets containing Lorem Ipsum passages, and more recently with desktop publishing software like Corvix PageForge including versions of Lorem Ipsum.</p>
  </div>
  <a class="btn dark" style="left:111px;top:467px;width:200px"><i class="face"></i><i class="stripe"></i><span>Get Started</span></a>
</section>

<section class="customers">
  <h2 class="section-title" style="top:80px">HAPPY CUSTOMERS</h2>
  <p class="section-lead" style="top:152px">Lorem Ipsum is simply dummy text of the printing and typesetting industry. Lorem Ipsum has been the industry's standard dummy text<br>ever since the 1500s, when an unknown printer took a galley of type and scrambled</p>

  <article class="review" style="left:111px">
    <svg width="40" height="34" viewBox="0 0 40 34" aria-hidden="true"><path d="M2 34V18C2 8 7 2 16 0l1 5c-5 2-7 5-7 10h7v19zM23 34V18c0-10 5-16 14-18l1 5c-5 2-7 5-7 10h7v19z" fill="var(--dark)"/></svg>
    <p class="quote">It is a long established fact that a reader will be distracted by the readable content of a page when looking at its layout. The point of using Lorem Ipsum is that it has a more-or-less normal distribution of letters, as opposed to using 'Content here, content here', making it look like readable English. Many desktop publishing packages and web page editors now use Lorem Ipsum as their default model text</p>
    <div class="name">- Daniel Ferro</div>
    <div class="place">Overland Park, KS</div>
  </article>
  <article class="review" style="left:615px">
    <svg width="40" height="34" viewBox="0 0 40 34" aria-hidden="true"><path d="M2 34V18C2 8 7 2 16 0l1 5c-5 2-7 5-7 10h7v19zM23 34V18c0-10 5-16 14-18l1 5c-5 2-7 5-7 10h7v19z" fill="var(--dark)"/></svg>
    <p class="quote">It is a long established fact that a reader will be distracted by the readable content of a page when looking at its layout. The point of using Lorem Ipsum is that it has a more-or-less normal distribution of letters, as opposed to using 'Content here, content here', making it look like readable English. Many desktop publishing packages and web page editors now use Lorem Ipsum as their default model text</p>
    <div class="name">- Daniel Ferro</div>
    <div class="place">Overland Park, KS</div>
  </article>

  <a class="btn" style="left:500px;top:668px;width:200px"><i class="face"></i><i class="stripe"></i><span>Read More</span></a>
</section>

<footer class="site-footer">
  <h2 class="newsletter-title">SUBSCRIBE TO OUR NEWSLETTER</h2>
  <form class="newsletter-form">
    <label>Email Address</label>
    <div class="send"><svg width="28" height="26" viewBox="0 0 28 26" aria-hidden="true"><path d="M1 12L27 1 20 25 13 16z" fill="#fff"/><path d="M13 16L27 1" stroke="var(--dark)" stroke-width="2"/></svg></div>
  </form>
  <div class="footer-brand">Kestral HVAC Supply</div>
  <nav class="footer-nav"><a>Home</a><i>|</i><a>About Us</a><i>|</i><a>Services</a><i>|</i><a>How It Works</a><i>|</i><a>Contact Us</a></nav>
  <p class="copyright">© Copyright 2023 Kestral HVAC Supply | All Rights Reserved.</p>
  <div class="socials"><span></span><span></span><span></span><span></span></div>
</footer>

</body>
</html>
```